Simple elegant business card

General card for a fin and television director.
Just want name, email, phone and address.

Target Market(s)

Prospective employers

Industry/Entity Type

Business

Requirements
Must have
• As above
Nice to have
• Logo but not necessary.
Should not have
• Not too colourful or funky.
• Simplicity and elegance the way to go.

```html
<!DOCTYPE html>
<html lang="en">
<head>
<meta charset="utf-8">
<title>Lena Marsh – Business Card</title>
<link href="https://fonts.googleapis.com/css2?family=Open+Sans:wght@400&display=swap" rel="stylesheet">
<style>
  :root {
    --backdrop: #e8e6e3;
    --card: #ffffff;
    --ink: #111111;
    --accent: #ec1c2b;
    --contact-band: #d2d3d5;
    --divider: #2b2a6b;
  }
  html, body {
    margin: 0;
    padding: 0;
    width: 1200px;
    height: 1200px;
    overflow: hidden;
    background: var(--backdrop);
    font-family: "Open Sans", Arial, sans-serif;
  }
  .canvas {
    position: relative;
    width: 1200px;
    height: 1200px;
  }
  .business-card {
    position: absolute;
    left: 78px;
    top: 420px;
    width: 1072px;
    height: 606px;
    background: var(--card);
    border-radius: 44px;
    box-shadow: 0 6px 24px rgba(0, 0, 0, 0.08);
  }
  .card-name {
    position: absolute;
    left: 162px;
    top: 151px;
    margin: 0;
    font-size: 138px;
    font-weight: 400;
    line-height: 1;
    letter-spacing: -1px;
    white-space: nowrap;
  }
  .name-first { color: var(--ink); }
  .name-last { color: var(--accent); }
  .contact-block {
    position: absolute;
    left: 378px;
    top: 372px;
    width: 678px;
    height: 126px;
    background: var(--contact-band);
    border-radius: 16px;
    overflow: hidden;
  }
  .contact-email,
  .contact-phone {
    position: absolute;
    left: 20px;
    margin: 0;
    color: var(--ink);
    white-space: nowrap;
    line-height: 1;
  }
  .contact-email {
    top: 8px;
    font-size: 50px;
  }
  .contact-divider {
    position: absolute;
    left: 0;
    right: 0;
    top: 65px;
    height: 5px;
    background: var(--divider);
  }
  .contact-phone {
    top: 83px;
    font-size: 35px;
    letter-spacing: 22px;
  }
</style>
</head>
<body>
  <main class="canvas">
    <section class="business-card">
      <h1 class="card-name"><span class="name-first">Lena</span><span class="name-last">Marsh</span></h1>
      <div class="contact-block">
        <p class="contact-email">lenamarsh@example.com</p>
        <div class="contact-divider"></div>
        <p class="contact-phone">+1 310 555 0147</p>
      </div>
    </section>
  </main>
</body>
</html>
```